THE HOMESTEAD PIVOT
Project: THE HOMESTEAD PIVOT
THE HOMESTEAD PIVOT  - Real Estate
Creative Brief
"THE HOMESTEAD PIVOT" is a new and upcoming real estate company. Very modern,Very Professional. With the help of Mark Craft Studio we now have company logo and stationary. We now need real estate yard signs...... We need a designer to take the company logo and other information and design a very professional, unique, modern yard sign that grabs your attention as you travel past. See attached picture for a normal yard sign. Note: The yard sign has two parts. Part one is an insert for individual name and phone number. Part two is the body of the sign with the words For Sale, logo and phone number. KEEP IN MIND - The sign frame will be forty two inches tall by twenty four inches wide. It will be taller than the normal yard sign. USE THE FOLLOWING INFORMATION ON SIGN: > CALVIN MORRISEY > 415-722-6143 > FOR SALE > LOGO - Ai file attached. THANKS FOR THE HELP.... GOOD LUCK.....
Real Estate
GENERAL PUBLIC IS AUDIENCE. STYLISH, PROFESSIONAL GRABS YOUR ATTENTION. MODERN
> USE COLOR SCHEME = IN LOGO AND STATIONARY. Ai file attached. > USE THIS INFORMATION: CALVIN MORRISEY 415-722-6143, FOR SALE, LOGO - Ai file attached.

```html
<!DOCTYPE html>
<html lang="en">
<head>
<meta charset="utf-8">
<title>The Homestead Pivot – Yard Sign</title>
<link href="https://fonts.googleapis.com/css2?family=Oswald:wght@500;700&display=swap" rel="stylesheet">
<style>
  :root {
    --backdrop: #eeeeec;
    --frame: #141414;
    --panel-dark: #1d1d1d;
    --accent-orange: #ee8a22;
    --sale-red: #d3231c;
    --cream: #f1e7c4;
    --cream-edge: #d9c78f;
    --brand-brown: #5a3a1c;
    --white: #ffffff;
  }
  * { margin: 0; padding: 0; box-sizing: border-box; }
  html, body {
    width: 1200px; height: 1014px; overflow: hidden;
    background: var(--backdrop);
    font-family: "Oswald", "Arial Narrow", sans-serif;
  }
  .canvas { position: relative; width: 1200px; height: 1014px; }

  .sign-frame {
    position: absolute; left: 0; top: 0;
  }

  .rider {
    position: absolute; left: 390px; top: 70px; width: 420px; height: 140px;
    background: var(--panel-dark);
    border: 6px solid var(--frame);
    display: flex; flex-direction: column; align-items: center; justify-content: center;
    gap: 4px;
  }
  .rider-mark {
    width: 34px; height: 34px; border-radius: 50%;
    background: var(--white);
  }
  .agent-name {
    color: var(--accent-orange); font-weight: 700; font-size: 34px;
    letter-spacing: 1px; line-height: 1;
  }
  .agent-phone {
    color: var(--white); font-weight: 700; font-size: 28px;
    letter-spacing: 1px; line-height: 1;
  }

  .sign-body {
    position: absolute; left: 390px; top: 222px; width: 420px; height: 600px;
    background: var(--panel-dark);
    border: 6px solid var(--frame);
    display: flex; flex-direction: column;
  }
  .sale-band {
    margin-top: 46px; height: 110px;
    background: var(--cream);
    display: flex; align-items: center; justify-content: center;
  }
  .sale-text {
    color: var(--sale-red); font-weight: 700; font-size: 84px;
    letter-spacing: 2px; line-height: 1;
  }
  .brand-area {
    flex: 1; margin: 24px 30px;
    background: var(--cream);
    border: 4px solid var(--cream-edge);
    display: flex; align-items: center; justify-content: center; gap: 14px;
  }
  .brand-dot {
    width: 30px; height: 30px; border-radius: 50%;
    background: var(--brand-brown); flex-shrink: 0;
  }
  .brand-name {
    color: var(--brand-brown); font-weight: 700; font-size: 34px;
    line-height: 1.05; text-align: center; letter-spacing: 1px;
  }
  .office-phone {
    height: 96px;
    display: flex; align-items: center; justify-content: center;
    color: var(--white); font-weight: 700; font-size: 50px; letter-spacing: 2px;
  }
</style>
</head>
<body>
<div class="canvas">
  <svg class="sign-frame" width="1200" height="1014" viewBox="0 0 1200 1014" aria-hidden="true">
    <rect x="402" y="200" width="10" height="760" fill="#141414"/>
    <rect x="788" y="200" width="10" height="760" fill="#141414"/>
    <rect x="390" y="206" width="420" height="20" fill="#141414"/>
  </svg>

  <div class="rider">
    <div class="rider-mark"></div>
    <div class="agent-name">CALVIN MORRISEY</div>
    <div class="agent-phone">415-722-6143</div>
  </div>

  <div class="sign-body">
    <div class="sale-band"><span class="sale-text">FOR SALE</span></div>
    <div class="brand-area">
      <span class="brand-dot"></span>
      <span class="brand-name">THE HOMESTEAD<br>PIVOT</span>
    </div>
    <div class="office-phone">415-722-6143</div>
  </div>
</div>
</body>
</html>
```